Tarrow Water Taxi and Transport Flyer

I need a business flyer for my new water taxi and freight transport business I have started here in Kodiak Alaska. Kodiak is a remote island in the middle of the gulf of Alaska. There are seven native villages around the island and Kodiak is the #2 fishing port in the United States. We also have the largest Coast Guard Base in the U.S.
My company will be providing water taxi and freight transport logistics to the villages and many hunting and fishing lodges as well as remote properties around the island.

I would like a business flyer that isn't status quo, something that stands out. I do like clean minimal designs but it needs to have the necessary contact info on it.

Target Market(s)

remote lodge / property owners, residents of the many villages around the island and anyone wanting to enjoy the great outdoors of Kodiak Alaska

Industry/Entity Type

Business

Colors
0355a3
0493ce
3277b5
9bcb3c
abd037
faa54b
f78f20
f37122
f68d4d

Requirements
Must have
• logo and necessary contact info
• Captain Morgan Haskell
• www.tarrowferrylink.com
• morgan@tarrowferrylink.com

```html
<!DOCTYPE html>
<html lang="en">
<head>
<meta charset="utf-8">
<title>Tarrow Water Taxi &amp; Transport Flyer</title>
<link href="https://fonts.googleapis.com/css2?family=Exo+2:ital,wght@0,300;0,400;0,600;0,700;1,300;1,400;1,700;1,800;1,900&family=Rajdhani:wght@500;700&family=Tinos:ital@1&display=swap" rel="stylesheet">
<style>
  :root {
    --navy: #0355a3;
    --sky: #0493ce;
    --mid-blue: #3277b5;
    --orange: #f37122;
    --orange-soft: #f78f20;
    --peach: #faa54b;
    --white: #ffffff;
    --ink: #1a2a3a;
    --stage: #e9ebee;
  }
  * { margin: 0; padding: 0; box-sizing: border-box; }
  html, body { width: 1200px; height: 900px; overflow: hidden; background: var(--stage); }
  .flyer {
    position: absolute; left: 285px; top: 10px;
    width: 629px; height: 880px; overflow: hidden;
    font-family: "Exo 2", sans-serif; color: var(--ink);
  }
  .flyer-bg { position: absolute; inset: 0; }
  .title {
    position: absolute; color: var(--white); white-space: nowrap;
    font-family: "Exo 2", sans-serif; font-style: italic; font-weight: 800;
    font-size: 62px; letter-spacing: -1px; line-height: 1;
    text-shadow: 0 2px 6px rgba(0,40,90,.25);
  }
  .title-main { left: 42px; top: 92px; }
  .title-sub { right: 42px; top: 178px; }
  .vessel-name {
    position: absolute; left: 163px; top: 378px; white-space: nowrap;
    font-family: "Rajdhani", sans-serif; font-weight: 700; font-size: 36px; color: var(--white);
  }
  .vessel-desc {
    position: absolute; left: 168px; top: 421px; width: 308px;
    font-size: 13px; line-height: 18.5px; color: #10273f; letter-spacing: -0.1px;
  }
  .captain-line {
    position: absolute; left: 43px; top: 519px; white-space: nowrap;
    font-family: "Rajdhani", sans-serif; font-weight: 700; font-size: 20px; color: var(--white);
  }
  .captain-name {
    position: absolute; right: 196px; top: 550px; white-space: nowrap;
    font-family: "Rajdhani", sans-serif; font-weight: 700; font-size: 16px; color: var(--navy);
  }
  .speed-note {
    position: absolute; left: 492px; top: 542px; white-space: nowrap;
    font-family: "Tinos", serif; font-style: italic; font-size: 11.5px; line-height: 16px; color: var(--white);
  }
  .inside-heading {
    position: absolute; left: 43px; top: 604px;
    font-weight: 400; font-size: 34px; color: var(--orange);
  }
  .feature-list {
    position: absolute; left: 43px; top: 661px; list-style: none; white-space: nowrap;
    font-style: italic; font-weight: 300; font-size: 14px; line-height: 24.5px; color: #1c1c1c;
  }
  .feature-list li::before { content: "•"; color: var(--navy); margin-right: 8px; font-style: normal; }
  .service-promise {
    position: absolute; left: 351px; top: 650px; white-space: nowrap;
    font-style: italic; font-weight: 900; font-size: 20px; line-height: 23px; color: var(--navy);
    letter-spacing: .5px;
  }
  .brand {
    position: absolute; left: 22px; top: 820px; display: flex; align-items: center; gap: 5px;
    font-family: "Exo 2", sans-serif; font-weight: 700; font-size: 17px; color: var(--navy);
  }
  .brand-dot { width: 10px; height: 10px; border-radius: 50%; background: var(--sky); }
  .contact-heading {
    position: absolute; left: 300px; top: 832px; white-space: nowrap;
    font-style: italic; font-weight: 700; font-size: 20px; color: var(--white);
  }
  .contact-details {
    position: absolute; left: 412px; top: 812px; white-space: nowrap;
    font-size: 11.5px; line-height: 18px; color: var(--white);
  }
</style>
</head>
<body>
<main class="flyer">
  <svg class="flyer-bg" viewBox="0 0 629 880" width="629" height="880">
    <defs>
      <linearGradient id="sceneryTone" x1="0" y1="0" x2="0" y2="1">
        <stop offset="0" stop-color="#2a86d0"/>
        <stop offset=".55" stop-color="#8cc4ec"/>
        <stop offset=".62" stop-color="#dfeaf4"/>
        <stop offset=".66" stop-color="#2c6fb3"/>
        <stop offset="1" stop-color="#1a5fa6"/>
      </linearGradient>
      <linearGradient id="bandTone" x1="0" y1="0" x2="1" y2="1">
        <stop offset="0" stop-color="#8bd0f0"/>
        <stop offset=".5" stop-color="#3a9ad8"/>
        <stop offset="1" stop-color="#1d88d0"/>
      </linearGradient>
      <linearGradient id="orangeBand" x1="0" y1="0" x2="1" y2="0">
        <stop offset="0" stop-color="#e8691c"/>
        <stop offset=".5" stop-color="#faa54b"/>
        <stop offset="1" stop-color="#f37122"/>
      </linearGradient>
      <linearGradient id="contactBand" x1="0" y1="0" x2="1" y2="0">
        <stop offset="0" stop-color="#faa54b"/>
        <stop offset=".45" stop-color="#f37122"/>
        <stop offset="1" stop-color="#a9501b"/>
      </linearGradient>
      <linearGradient id="vesselTone" x1="0" y1="0" x2="0" y2="1">
        <stop offset="0" stop-color="#9aa4ad"/>
        <stop offset="1" stop-color="#3d454d"/>
      </linearGradient>
    </defs>
    <rect class="scenery-photo" x="0" y="0" width="629" height="520" fill="url(#sceneryTone)" role="img" aria-label="Photo of calm blue sea with snow-capped mountains under a bright sky"/>
    <path class="top-wave" d="M0 0H629V10C560 32 470 2 380 22C300 40 200 12 120 22C60 30 20 52 0 62Z" fill="#5aaae3" opacity=".85"/>
    <path class="vessel-band" d="M0 452C60 392 160 372 260 372C400 372 520 362 629 356V880H0Z" fill="url(#bandTone)"/>
    <rect class="vessel-photo" x="486" y="432" width="134" height="84" rx="12" fill="url(#vesselTone)" role="img" aria-label="Photo of the aluminium landing-craft vessel on the water"/>
    <path class="captain-band" d="M0 500C100 480 200 478 300 495C380 510 440 535 484 565C400 590 330 595 268 592C170 590 80 575 0 560Z" fill="url(#orangeBand)"/>
    <path class="content-area" d="M0 560C80 575 170 590 268 592C330 595 400 590 484 565C540 600 590 640 629 668V880H0Z" fill="#ffffff"/>
    <path class="logo-wave" d="M0 808C30 778 80 770 120 795C150 815 170 860 205 880H0Z" fill="#b7e3ea"/>
    <path class="contact-band" d="M210 880C260 850 330 815 420 800C500 790 580 795 629 778V880Z" fill="url(#contactBand)"/>
  </svg>

  <h1 class="title title-main">Tarrow Water Taxi</h1>
  <div class="title title-sub">&amp; Transport</div>

  <h2 class="vessel-name">The Heron Point</h2>
  <p class="vessel-desc">carrying up to 5,000 pounds and 6 passengers. Vessel is equipped with extra large fuel tanks and powerful and fuel efficient outboards</p>

  <p class="captain-line">A knowledgeable and friendly captain</p>
  <p class="captain-name">Captain Morgan Haskell</p>
  <p class="speed-note">Cruise speed between<br>20 and 24 miles per hour.</p>

  <h2 class="inside-heading">What’s inside</h2>
  <ul class="feature-list">
    <li>Comfortable cabin with heat, bathroom</li>
    <li>Pick up or drop off to and from your location</li>
    <li>Surround sound stereo with blue tooth</li>
    <li>Large front deck for cargo or wild life viewing</li>
  </ul>
  <p class="service-promise">All of our clients<br>are provided with<br>highest level of<br>customer service</p>

  <div class="brand"><span class="brand-dot"></span>TARROW</div>

  <p class="contact-heading">Contact us</p>
  <p class="contact-details">tel: 907-555-0148<br>email: morgan@tarrowferrylink.com<br>www.tarrowferrylink.com</p>
</main>
</body>
</html>
```